Brackenfold Roofing Business Card

Need a business card with the logo that was designed here

Contact Information for Business Card

Name, Title, Phone, Email, Website, Company name

```html
<!DOCTYPE html>
<html lang="en">
<head>
<meta charset="utf-8">
<title>Brackenfold Roofing Business Card</title>
<link rel="stylesheet" href="https://fonts.googleapis.com/css2?family=Montserrat:wght@800&family=Poppins:wght@400;600&display=swap">
<style>
  :root {
    --stage: #c7c7c7;
    --card-white: #ffffff;
    --brand-blue: #1f7ac4;
    --brand-blue-light: #1e98f5;
    --brand-blue-deep: #1a63a8;
    --ink: #3a3a3a;
    --divider: #cfcfcf;
  }
  * { box-sizing: border-box; margin: 0; padding: 0; }
  html, body {
    width: 1200px; height: 800px; overflow: hidden;
    background: var(--stage);
  }
  .stage {
    position: relative; width: 1200px; height: 800px;
    display: flex; align-items: center; justify-content: center; gap: 40px;
  }
  .card {
    position: relative; width: 520px; height: 298px;
    border-radius: 2px; overflow: hidden;
    box-shadow: 0 10px 30px rgba(0,0,0,0.25);
  }

  /* Front */
  .card--front {
    background: var(--card-white);
    border-bottom: 3px solid var(--brand-blue);
    display: flex; align-items: center;
  }
  .front__brand {
    width: 240px; height: 100%; flex: none;
    display: flex; align-items: center; justify-content: center;
    padding: 0 24px;
  }
  .wordmark {
    font-family: "Poppins", sans-serif; font-weight: 600;
    font-size: 24px; line-height: 1.15; color: var(--brand-blue);
    display: flex; align-items: center; gap: 10px;
  }
  .wordmark__square {
    width: 14px; height: 14px; background: var(--brand-blue); flex: none;
  }
  .front__divider {
    width: 1px; height: 170px; flex: none;
    background: linear-gradient(to bottom, transparent, var(--divider), transparent);
  }
  .front__contact {
    padding-left: 28px; padding-right: 16px;
    font-family: "Poppins", sans-serif; color: var(--ink);
  }
  .person__name {
    font-family: "Montserrat", sans-serif; font-weight: 800;
    font-size: 19px; color: var(--brand-blue); letter-spacing: 0.3px;
    text-transform: uppercase; white-space: nowrap;
  }
  .person__title { font-size: 13px; color: var(--ink); margin-bottom: 18px; }
  .contact-list { list-style: none; }
  .contact-list li {
    display: flex; align-items: center; gap: 9px;
    font-size: 13px; line-height: 1.75; white-space: nowrap;
  }
  .contact-list svg { width: 13px; height: 13px; fill: var(--brand-blue); flex: none; }
  .accent { color: var(--brand-blue); }

  /* Back */
  .card--back {
    background: var(--brand-blue);
    display: flex; align-items: center; justify-content: center;
  }
  .back__backdrop {
    position: absolute; inset: 0;
    background: linear-gradient(160deg, var(--brand-blue-light) 0%, var(--brand-blue) 55%, var(--brand-blue-deep) 100%);
  }
  .back__wordmark {
    position: relative;
    font-family: "Poppins", sans-serif; font-weight: 600;
    font-size: 34px; color: var(--card-white);
    display: flex; align-items: center; gap: 12px; white-space: nowrap;
  }
  .back__square { width: 16px; height: 16px; background: var(--card-white); flex: none; }
</style>
</head>
<body>
<main class="stage">
  <section class="card card--front">
    <div class="front__brand">
      <p class="wordmark"><span class="wordmark__square"></span><span>Brackenfold<br>Roofing</span></p>
    </div>
    <div class="front__divider"></div>
    <div class="front__contact">
      <h1 class="person__name">Devlin Ashcombe</h1>
      <p class="person__title">Managing Director</p>
      <ul class="contact-list">
        <li>
          <svg viewBox="0 0 24 24" aria-hidden="true"><path d="M6.6 10.8a15.1 15.1 0 0 0 6.6 6.6l2.2-2.2a1 1 0 0 1 1-.25 11.4 11.4 0 0 0 3.6.57 1 1 0 0 1 1 1V20a1 1 0 0 1-1 1A17 17 0 0 1 3 4a1 1 0 0 1 1-1h3.5a1 1 0 0 1 1 1c0 1.25.2 2.45.57 3.6a1 1 0 0 1-.25 1z"/></svg>
          044-987 210 543
        </li>
        <li>
          <svg viewBox="0 0 24 24" aria-hidden="true"><path d="M2 5h20v14H2z M2 5l10 8 10-8" fill="none" stroke="#1f7ac4" stroke-width="2"/></svg>
          info@brackenfoldroof.com
        </li>
        <li>
          <svg viewBox="0 0 24 24" aria-hidden="true"><path d="M12 2a10 10 0 1 0 0 20 10 10 0 0 0 0-20zm6.9 6h-3a15.7 15.7 0 0 0-1.3-3.9A8 8 0 0 1 18.9 8zM12 4c.8 1.2 1.5 2.5 1.9 4h-3.8c.4-1.5 1.1-2.8 1.9-4zM4.3 14a8 8 0 0 1 0-4h3.4a16.5 16.5 0 0 0 0 4zm.8 2h3a15.7 15.7 0 0 0 1.3 3.9A8 8 0 0 1 5.1 16zm3-8h-3a8 8 0 0 1 4.3-3.9A15.7 15.7 0 0 0 8.1 8zM12 20c-.8-1.2-1.5-2.5-1.9-4h3.8c-.4 1.5-1.1 2.8-1.9 4zm2.3-6H9.7a14.7 14.7 0 0 1 0-4h4.6a14.7 14.7 0 0 1 0 4zm.3 5.9a15.7 15.7 0 0 0 1.3-3.9h3a8 8 0 0 1-4.3 3.9zm1.7-5.9a16.5 16.5 0 0 0 0-4h3.4a8 8 0 0 1 0 4z"/></svg>
          <span>www.<span class="accent">brackenfoldroofing</span>.com</span>
        </li>
      </ul>
    </div>
  </section>

  <section class="card card--back">
    <div class="back__backdrop" role="img" aria-label="Blue background with a large stylised house roof, chimney and window decoration"></div>
    <p class="back__wordmark"><span class="back__square"></span>Brackenfold Roofing</p>
  </section>
</main>
</body>
</html>
```